New Business Card

We need to refresh our business cards. We designed these ourselves and we have no graphic design experience. We would like to find a new business card design that is professional and unique. We are an auto finance company. Feel free to play with the logo, but we would like to keep the eye very present on the card. Our corporate colors are green, grey, and white.
Green - RGB - 168,215,27; HEX - #AADD22
Grey - RGB - 196,196,196; HEX - #C4C4C4
Need to upload the vector file to finalize the project. The last logo was for a jpeg that didn't stretch well.
Industry/Entity Type
Financial Service
Contact Information for Business Card
Honestly don't know...I need your help!

```html
<!DOCTYPE html>
<html lang="en">
<head>
<meta charset="utf-8">
<title>Northlane Capital – Business Card</title>
<link rel="stylesheet" href="https://fonts.googleapis.com/css2?family=Fira+Sans:wght@400;500;600&family=Source+Sans+3:wght@400&display=swap">
<style>
  :root {
    --green: #a8d71b;
    --grey: #c4c4c4;
    --paper: #e6e8e7;
    --charcoal: #3c3d41;
    --charcoal-light: #47484c;
    --ink: #5e6063;
    --backdrop: #a7a7a7;
  }
  * { box-sizing: border-box; margin: 0; padding: 0; }
  html, body {
    width: 1200px; height: 1200px; overflow: hidden;
    background: var(--backdrop);
  }
  .canvas { position: relative; width: 1200px; height: 1200px; }

  .card {
    position: absolute; left: 206px; width: 788px; height: 446px;
    border-radius: 26px; overflow: hidden;
  }
  .card--front { top: 96px; background: var(--paper); }
  .card--back {
    top: 658px;
    background: linear-gradient(135deg, var(--charcoal) 0%, var(--charcoal-light) 60%, var(--charcoal) 100%);
  }

  .brand {
    position: absolute; display: flex; align-items: center; gap: 14px;
    font-family: "Fira Sans", sans-serif; font-weight: 500;
    font-size: 40px; color: var(--green); white-space: nowrap;
  }
  .brand__dot {
    width: 26px; height: 26px; border-radius: 50%; background: var(--green); flex: none;
  }
  .card--front .brand { left: 56px; top: 196px; }
  .card--back .brand { left: 0; right: 0; top: 198px; justify-content: center; }

  .divider {
    position: absolute; left: 468px; top: 108px; width: 2px; height: 230px;
    background: var(--green);
  }
  .contact { position: absolute; left: 502px; top: 112px; }
  .contact__name {
    font-family: "Fira Sans", sans-serif; font-weight: 600;
    font-size: 27px; color: var(--green); letter-spacing: 0.5px; line-height: 1;
  }
  .contact__role, .contact__address, .contact__line {
    font-family: "Source Sans 3", sans-serif; font-size: 18px; color: var(--ink);
  }
  .contact__role { margin-top: 14px; }
  .contact__address { margin-top: 12px; line-height: 29px; }
  .contact__list { list-style: none; margin-top: 10px; }
  .contact__line { display: flex; align-items: center; gap: 10px; height: 28px; }
  .contact__icon { width: 15px; height: 15px; flex: none; }

  .wave { position: absolute; left: 0; bottom: 0; width: 788px; height: 446px; }

  .web {
    position: absolute; left: 0; right: 0; top: 386px; text-align: center;
    font-family: "Source Sans 3", sans-serif; font-size: 19px;
    color: #ffffff; letter-spacing: 1.5px;
  }
  .web__domain { color: var(--green); }
</style>
</head>
<body>
<main class="canvas">

  <section class="card card--front" aria-label="Business card front">
    <div class="brand"><span class="brand__dot"></span>Northlane Capital</div>

    <div class="divider"></div>

    <div class="contact">
      <h1 class="contact__name">DANIEL R. HAYES</h1>
      <p class="contact__role">Resident Manager</p>
      <p class="contact__address">Street Name Avenue, Suite<br>100 State, Zip Code,Country</p>
      <ul class="contact__list">
        <li class="contact__line">
          <svg class="contact__icon" viewBox="0 0 16 16"><path fill="#a8d71b" d="M3.5 1l3 3-1.8 1.8c.9 2 2.5 3.6 4.5 4.5L11 8.5l3 3-2 2.5C6.5 13.5 2.5 9.5 1 3.5z"/></svg>
          555-014-2738
        </li>
        <li class="contact__line">
          <svg class="contact__icon" viewBox="0 0 16 16"><g fill="#a8d71b"><rect x="4" y="1" width="8" height="4"/><rect x="1" y="6" width="14" height="6" rx="1"/><rect x="4" y="10" width="8" height="5" fill="#e6e8e7" stroke="#a8d71b" stroke-width="1.5"/></g></svg>
          555-017-4461
        </li>
        <li class="contact__line">
          <svg class="contact__icon" viewBox="0 0 16 16"><g fill="none" stroke="#a8d71b" stroke-width="1.6"><rect x="1" y="3" width="14" height="10"/><path d="M1 3l7 6 7-6"/></g></svg>
          info@northlanecapital.com
        </li>
        <li class="contact__line">
          <svg class="contact__icon" viewBox="0 0 16 16"><g fill="none" stroke="#a8d71b" stroke-width="1.4"><circle cx="8" cy="8" r="6.5"/><ellipse cx="8" cy="8" rx="3" ry="6.5"/><path d="M1.5 8h13M2.5 5h11M2.5 11h11"/></g></svg>
          www.northlanecapital.com
        </li>
      </ul>
    </div>

    <svg class="wave" viewBox="0 0 656 372" preserveAspectRatio="none" aria-hidden="true">
      <path fill="#ffffff" d="M0 324 C120 340 220 356 320 348 C450 336 560 330 656 332 L656 372 L0 372 Z"/>
      <path fill="#3c3d41" d="M0 332 C120 347 220 362 320 355 C450 345 560 338 656 340 L656 372 L0 372 Z"/>
      <path fill="#a8d71b" d="M0 312 C90 330 200 348 300 351 C200 353 90 342 0 326 Z"/>
      <path fill="#a8d71b" d="M360 340 C460 330 560 323 656 322 L656 334 C560 333 460 336 360 340 Z"/>
    </svg>
  </section>

  <section class="card card--back" aria-label="Business card back">
    <div class="brand"><span class="brand__dot"></span>Northlane Capital</div>
    <p class="web">www.<span class="web__domain">northlanecapital</span>.com</p>
  </section>

</main>
</body>
</html>
```